Emerging Australian photographer

I'm based in Cunderdin, a small rural town in the Wheatbelt area of Western Australia. So its a good thing that I love to travel further afield both for pleasure and for work. To me that is one and the same thing in any event!

My desire is to take photos that make the viewers heart skip. I love taking photos of people doing the things they love or being with the people they love. For me, the joy of photography comes with capturing the 'moments between the moments'. I like candid photography best of all - like when the new husband is staring joyfully at his bride and at that minute is unaware of the photographer capturing the moment.

I am available for weddings, engagements, birthdays, special events, newborns, family or individual portraits. By the end of the year I will be accredited with the Southern Guild of Practising Imagemakers.

I need a card that stands out but is elegant and would sit well on the table at a wedding or be given out in the church grounds. Classy and a little bit sassy.

Target Market(s)

Consumers who are seeking photographic services, eg wedding guests who see me at work and make enquiries.

Industry/Entity Type

Church

Contact Information for Business Card

Danielle Whitcombe Photography
Danielle Whitcombe
0438 562 073
www.daniellewhitcombe.com.au
photos@daniellewhitcombe.com.au

Requirements
Must have
• Must fit with the theme in the watermarks, but be crisp and modern.
Nice to have
• However it's not essential to have the pink! Chatterbook and Pipsqueak logos.
Should not have
• Old style fonts like times new roman.

```html
<!DOCTYPE html>
<html lang="en">
<head>
<meta charset="utf-8">
<title>Danielle Whitcombe Photography – Business Card</title>
<link rel="stylesheet" href="https://fonts.googleapis.com/css2?family=Arimo:wght@400;700&display=swap">
<style>
  :root {
    --backdrop: #e9e7e4;
    --card: #f7f7f6;
    --ink: #5f5f61;
    --ink-soft: #8a8a8c;
    --blush: #f08cb4;
    --shadow: rgba(40, 35, 30, 0.18);
  }
  * { margin: 0; padding: 0; box-sizing: border-box; }
  html, body {
    width: 916px;
    height: 1200px;
    overflow: hidden;
    background: var(--backdrop);
    font-family: "Arimo", Arial, sans-serif;
    color: var(--ink);
  }
  .sheet {
    width: 916px;
    height: 1200px;
    display: flex;
    flex-direction: column;
    align-items: center;
    justify-content: center;
    gap: 80px;
  }
  .card {
    position: relative;
    width: 760px;
    height: 464px;
    background: var(--card);
    border-radius: 22px;
    box-shadow: 0 10px 28px var(--shadow);
  }

  /* Front */
  .card-front {
    display: flex;
    flex-direction: column;
    align-items: center;
    justify-content: center;
  }
  .brand {
    display: flex;
    align-items: center;
    gap: 14px;
  }
  .brand-dot {
    width: 14px;
    height: 14px;
    border-radius: 50%;
    background: var(--blush);
  }
  .brand-name {
    font-size: 40px;
    font-weight: 400;
    color: var(--ink);
    letter-spacing: 0.5px;
  }
  .website {
    margin-top: 46px;
    font-size: 17px;
    letter-spacing: 5px;
    color: var(--ink-soft);
  }
  .website .domain { color: var(--blush); }

  /* Back */
  .card-back .brand {
    position: absolute;
    top: 88px;
    left: 50%;
    transform: translateX(-50%);
    white-space: nowrap;
  }
  .card-back .brand-name { font-size: 30px; }
  .card-back .brand-dot { width: 11px; height: 11px; }
  .contact-block {
    position: absolute;
    left: 220px;
    top: 196px;
  }
  .person-name {
    font-size: 38px;
    font-weight: 400;
    line-height: 1;
  }
  .person-name .first { color: var(--blush); }
  .person-name .last { color: var(--ink); }
  .role {
    margin-top: 6px;
    font-size: 17px;
    letter-spacing: 7px;
    color: var(--blush);
  }
  .details {
    margin-top: 34px;
    font-size: 16px;
    line-height: 1.55;
    color: var(--ink);
  }
  .details .label { color: var(--blush); margin-right: 6px; }
</style>
</head>
<body>
  <main class="sheet">
    <section class="card card-front" aria-label="Card front">
      <div class="brand">
        <span class="brand-dot"></span>
        <span class="brand-name">Danielle Whitcombe Photography</span>
      </div>
      <p class="website">www.<span class="domain">daniellewhitcombe</span>.com.au</p>
    </section>

    <section class="card card-back" aria-label="Card back">
      <div class="brand">
        <span class="brand-dot"></span>
        <span class="brand-name">Danielle Whitcombe Photography</span>
      </div>
      <div class="contact-block">
        <h1 class="person-name"><span class="first">Danielle</span> <span class="last">Whitcombe</span></h1>
        <p class="role">Photographer</p>
        <p class="details">
          <span class="label">Phone</span>0438 562 073<br>
          photos@daniellewhitcombe.com.au
        </p>
      </div>
    </section>
  </main>
</body>
</html>
```